Green Logistics / Last Mile Delivery Firm needs cool one-page website

FYI - We do have a detailed brief in the uploaded files section below
COMPANY
We recently launched the company Brook Logistics which is a pioneer in urban green logistics and provides zero-emissions last mile delivery services (i.e. delivery of parcels with delivery vans to the doorstep of households) for its logistics and retail clients.
We take on urban parcel delivery for our clients with a 100% electric commercial vehicles fleet, fair and sustainable working conditions for our employees and an unparalleled professional and customer-focused mindset.
WEBSITE
In the detailed brief, we have provided examples to emulate. We need the design + coding of the website. Website needs to be friendly/optimized for and should open swiftly on both Android & iOS.
In general, the website should convey
- green mission of the company
- sustainability (good working conditions, focus on employees)
- customer orientation
- professionalism
DESIGN
In the detailed brief, we have provided designs to emulate.
Color design: we do have a logo which features 2 green colors (one lighter and one darker color tone). However, the colors on the website do not necessarily need to follow these 2 colors exactly as we are able to switch the logo colors.
Imagery: should reflect maybe 50% green/leaf/tree , 25% customer and employee orientation, and 25% logistics (here it's important that it is the last mile delivery, i.e. delivery with delivery vans to the doorstep of households)
Coding

```html
<!DOCTYPE html>
<html lang="en">
<head>
<meta charset="utf-8">
<title>Brook Logistics – Sustainable Last Mile</title>
<link rel="stylesheet" href="https://fonts.googleapis.com/css2?family=Jost:wght@400;500;600&display=swap">
<style>
:root{
  --green:#1f9a3f;
  --green-dark:#17803a;
  --lime:#8cc63f;
  --ink:#1d1d1d;
  --text:#5b5b5b;
  --muted:#8a8a8a;
  --line:#e3e6e8;
  --bg-soft:#eef2f5;
  --white:#ffffff;
}
*{box-sizing:border-box;margin:0;padding:0}
html,body{width:1200px;height:4112px;overflow:hidden}
body{position:relative;font-family:"Jost",sans-serif;color:var(--text);background:var(--white)}
.abs{position:absolute}
.center{text-align:center}
h2.section-title{position:absolute;left:0;width:1200px;text-align:center;font-weight:400;font-size:38px;color:var(--ink)}
.btn{position:absolute;display:flex;align-items:center;justify-content:center;border-radius:16px;color:var(--white);font-size:14px;font-weight:500}

/* header + hero */
.hero{position:absolute;left:0;top:0;width:1200px;height:640px;background:linear-gradient(160deg,#3a3f33 0%,#5b634b 40%,#2c3026 100%)}
.hero::after{content:"";position:absolute;inset:0;background:rgba(20,20,20,.35)}
.site-header{position:absolute;left:0;top:0;width:1200px;height:96px;border-bottom:1px solid rgba(255,255,255,.2);z-index:2}
.brand{position:absolute;left:32px;top:32px;display:flex;align-items:center;gap:10px;color:var(--lime);font-size:22px;font-weight:600;letter-spacing:.5px}
.brand-dot{width:26px;height:26px;border-radius:50%;background:var(--lime)}
.nav a{position:absolute;top:38px;color:var(--white);font-size:14px;text-decoration:none}
.nav a.active{color:var(--lime)}
.nav-underline{position:absolute;left:452px;top:94px;width:52px;height:2px;background:var(--lime)}
.call{position:absolute;left:851px;top:38px;font-size:14px;color:var(--white)}
.call span{color:var(--lime)}
.mail-btn{position:absolute;left:1040px;top:33px;width:28px;height:28px;border-radius:50%;border:1px solid var(--white);display:flex;align-items:center;justify-content:center}
.lang{position:absolute;left:1080px;top:32px;width:88px;height:30px;border-radius:15px;background:var(--green);color:var(--white);font-size:12px;display:flex;align-items:center;justify-content:center;gap:10px}
.hero-content{position:absolute;left:0;top:290px;width:1200px;text-align:center;color:var(--white);z-index:2}
.hero-content h1{font-weight:500;font-size:40px}
.hero-content p{font-size:22px;margin-top:12px}
.hero .btn{left:538px;top:405px;width:126px;height:30px;background:var(--lime);z-index:2}
.arrow{position:absolute;top:350px;z-index:2}

/* about */
.about{position:absolute;left:0;top:640px;width:1200px;height:925px;background:var(--bg-soft)}
.card{position:absolute;top:788px;width:320px;height:495px;background:var(--white);box-shadow:0 2px 10px rgba(0,0,0,.06)}
.card-photo{height:200px;width:100%}
.card-badge{position:absolute;left:38px;top:168px;width:64px;height:64px;border-radius:50%;background:var(--white);display:flex;align-items:center;justify-content:center}
.card-badge span{width:34px;height:34px;border-radius:50%;background:var(--lime)}
.card h3{font-weight:500;font-size:16px;color:var(--ink);margin:58px 24px 14px;letter-spacing:.5px}
.card p{font-size:11.5px;line-height:17.5px;margin:0 24px 16px}

/* tree-logistics-is */
.compare{position:absolute;left:88px;top:1365px;width:1024px;height:415px;background:linear-gradient(120deg,#ffffff 0%,#f3f8fd 50%,#e6f0f6 100%);box-shadow:0 2px 12px rgba(0,0,0,.06);overflow:hidden}
.compare-leaf{position:absolute;left:0;top:0;width:210px;height:170px;background:radial-gradient(ellipse at 40% 40%,#2f7a2a,#5aa33c 55%,transparent 72%)}
.compare-fern{position:absolute;right:0;bottom:0;width:180px;height:240px;background:radial-gradient(ellipse at 80% 80%,#a9c39a,transparent 70%)}
.compare h2{position:absolute;left:0;top:34px;width:100%;text-align:center;font-weight:400;font-size:38px;color:var(--ink)}
.compare-divider{position:absolute;left:512px;top:110px;width:1px;height:230px;background:var(--line)}
.col-left{position:absolute;right:544px;top:190px;text-align:right}
.col-right{position:absolute;left:552px;top:190px}
.col-left h3,.col-right h3{font-weight:500;font-size:19px;color:var(--ink);margin-bottom:16px}
.col-right h3{color:var(--green)}
.col-left li,.col-right li{list-style:none;font-size:12px;line-height:22.5px}
.col-left li{text-decoration:line-through}

/* services */
.svc{position:absolute;top:1928px;width:232px;height:271px;border:1px solid var(--line);text-align:center;background:var(--white)}
.svc.raised{box-shadow:0 4px 14px rgba(0,0,0,.1);border-color:transparent}
.svc-icon{margin:32px auto 0;width:80px;height:80px;border-radius:50%;display:flex;align-items:center;justify-content:center}
.svc h3{font-weight:500;font-size:16px;color:var(--ink);margin:22px 24px 12px;line-height:21px}
.svc p{font-size:11.5px;line-height:17.5px;margin:0 30px;color:var(--muted)}

/* touch */
.touch{position:absolute;left:0;top:2279px;width:1200px;height:311px;background:linear-gradient(100deg,#4b6a40 0%,#6d8b59 50%,#3f5a36 100%)}
.touch h2{position:absolute;left:0;top:74px;width:100%;text-align:center;font-weight:400;font-size:38px;color:var(--white)}
.touch p{position:absolute;left:200px;top:130px;width:800px;text-align:center;font-size:13px;line-height:24px;color:var(--white)}
.touch .btn{left:538px;top:203px;width:126px;height:28px;background:var(--green)}

/* careers */
.careers-text{position:absolute;left:168px;width:864px;font-size:12px;line-height:17.5px}
.leaf-left{position:absolute;left:0;top:2780px;width:130px;height:130px;background:radial-gradient(ellipse at 50% 50%,#5ea92f,transparent 70%)}
.leaf-right{position:absolute;left:1040px;top:3110px;width:160px;height:150px;background:radial-gradient(ellipse at 60% 50%,#2d7d25,transparent 70%)}
.acc{position:absolute;left:168px;width:864px;border-bottom:1px solid var(--line)}
.acc h4{font-weight:500;font-size:13px;color:var(--ink)}
.acc p{font-size:11.5px;line-height:16px;margin-top:10px;width:620px}
.acc .plus{position:absolute;right:22px;top:-4px;color:var(--green);font-size:24px;line-height:24px;font-weight:400}

/* contact */
.contact{position:absolute;left:0;top:3245px;width:1200px;height:867px;background:linear-gradient(180deg,#eeeeee 0%,#e2e6dc 40%,#9fb883 70%,#55803a 100%)}
.contact-icon{position:absolute;top:3439px;width:80px;height:80px;border-radius:50%;border:2px solid var(--green);display:flex;align-items:center;justify-content:center}
.contact-label{position:absolute;top:3534px;width:240px;text-align:center;font-size:12px;line-height:20px;color:var(--ink)}
.field{position:absolute;background:var(--white);font-size:12px;color:var(--muted);padding:8px 16px;border:1px solid #e5e5e5}
.contact .btn{position:absolute}
.footer-line{position:absolute;left:88px;top:3894px;width:1024px;height:1px;background:rgba(255,255,255,.5)}
.social{position:absolute;top:3936px;width:28px;height:28px;border-radius:50%;background:var(--green)}
.footer-nav{position:absolute;left:0;top:3994px;width:1200px;display:flex;justify-content:center;gap:30px;font-size:14px;color:var(--white)}
.copyright{position:absolute;left:0;top:4036px;width:1200px;text-align:center;font-size:11px;color:var(--white)}
</style>
</head>
<body>

<section class="hero" role="img" aria-label="Photo of a bright room with green indoor plants"></section>
<header class="site-header">
  <div class="brand"><span class="brand-dot"></span>BROOK LOGISTICS</div>
  <nav class="nav">
    <a class="active" style="left:460px">Home</a>
    <a style="left:528px">About</a>
    <a style="left:597px">Services</a>
    <a style="left:680px">Careers</a>
    <a style="left:760px">Contact</a>
  </nav>
  <div class="nav-underline"></div>
  <div class="call"><span>Call Us: ✆</span> +123-456-7890</div>
  <div class="mail-btn"><svg width="12" height="10" viewBox="0 0 12 10"><rect x=".5" y=".5" width="11" height="9" fill="none" stroke="#fff"/><path d="M.5 .5 6 5l5.5-4.5" fill="none" stroke="#fff"/></svg></div>
  <div class="lang">ENG <svg width="9" height="6" viewBox="0 0 9 6"><path d="M1 1l3.5 3.5L8 1" fill="none" stroke="#fff" stroke-width="1.3"/></svg></div>
</header>
<svg class="arrow" style="left:88px" width="20" height="36" viewBox="0 0 20 36"><path d="M18 2 2 18l16 16" fill="none" stroke="#fff" stroke-width="2.5"/></svg>
<svg class="arrow" style="left:1092px" width="20" height="36" viewBox="0 0 20 36"><path d="M2 2l16 16L2 34" fill="none" stroke="#fff" stroke-width="2.5"/></svg>
<div class="hero-content">
  <h1>Brook Logistics – Sustainable Last Mile</h1>
  <p>Because we care about trees!</p>
</div>
<div class="hero"><div class="btn" style="background:var(--lime)">Get Started</div></div>

<section class="about"></section>
<h2 class="section-title" style="top:710px">About Us</h2>

<article class="card" style="left:88px">
  <div class="card-photo" role="img" aria-label="Photo of a white delivery truck on a highway" style="background:linear-gradient(180deg,#b8cde0,#8a9aa5 60%,#6e7a70)"></div>
  <div class="card-badge"><span></span></div>
  <h3>Who We Are</h3>
  <p>Brook Logistics is a pioneer in urban green logistics and provides zeroemissions last mile delivery services for its logistics and retail clients.</p>
  <p>We take on urban parcel delivery for our clients with a 100% electric commercial vehicles fleet, fair and sustainable working conditions for our employees and an unparalleled professional and customer-focused mindset.</p>
</article>
<article class="card" style="left:440px">
  <div class="card-photo" role="img" aria-label="Photo of a smiling florist among potted plants" style="background:linear-gradient(180deg,#e6ebe8,#a8b8a0 60%,#5e7a4c)"></div>
  <div class="card-badge"><span></span></div>
  <h3>Our Mission</h3>
  <p>To satisfy consumers' ever-rising desire to buy products online, the CO2 emissions from delivery traffic will increase by 32% in the top 100 cities globally until 2030.</p>
  <p>Our clients care about our planet the same way we do, which is why Brook Logistics helps to make the planet a better place by running the most environmentally friendly urban last mile possible.</p>
</article>
<article class="card" style="left:792px">
  <div class="card-photo" role="img" aria-label="Photo of a courier holding roses and a clipboard" style="background:linear-gradient(135deg,#e8735a,#c9422f 45%,#2f6a3a)"></div>
  <div class="card-badge"><span></span></div>
  <h3>Our values</h3>
  <p>We see ourselves as a professional services company who strongly cares about the environment, its clients and their customers, as well as its employees.</p>
  <p>We believe that delivering parcels with zero emissions and providing a unique customer experience through a highly professional attitude and a great team spirit are the cornerstones for Brook Logistics to operate in today's world in a sustainable yet profitable way.</p>
</article>

<section class="compare">
  <div class="compare-leaf" role="img" aria-label="Monstera leaf"></div>
  <div class="compare-fern" role="img" aria-label="Soft fern leaves"></div>
  <h2>Brook Logistics is...</h2>
  <svg class="abs" style="left:415px;top:120px" width="58" height="56" viewBox="0 0 58 56"><path d="M29 3 54 15v27L29 54 4 42V15z M4 15l25 12 25-12 M29 27v27 M16 9l25 12v10" fill="none" stroke="#1d1d1d" stroke-width="3" stroke-linejoin="round"/></svg>
  <svg class="abs" style="left:552px;top:120px" width="100" height="52" viewBox="0 0 100 52"><g fill="none" stroke="#1f9a3f" stroke-width="3" stroke-linejoin="round"><path d="M30 6h38v34H30z M68 18h16l12 12v10H68"/><circle cx="42" cy="44" r="5"/><circle cx="82" cy="44" r="5"/><path d="M2 14h20 M8 22h16 M2 30h20"/></g></svg>
  <div class="compare-divider"></div>
  <div class="col-left">
    <h3>An Ordinary Parcel Delivery Firm</h3>
    <ul><li>Polluting our cities</li><li>Always in a rush</li><li>Short-term oriented</li><li>Focusing on profit only</li><li>Yet another parcel delivery firm</li></ul>
  </div>
  <div class="col-right">
    <h3>A Pioneering Green Last Mile</h3>
    <ul><li>Delivering parcels emissions-free</li><li>Putting customer experience first</li><li>Operating the business sustainably</li><li>Focusing on the environment, customers and employees</li><li>A professional services company</li></ul>
  </div>
</section>

<h2 class="section-title" style="top:1850px">Our Services</h2>
<article class="svc" style="left:88px">
  <div class="svc-icon" style="background:var(--green)"><svg width="44" height="34" viewBox="0 0 44 34"><g fill="none" stroke="#fff" stroke-width="2.2"><path d="M2 4h26v22H2z M28 12h8l6 7v7H28"/><circle cx="10" cy="28" r="3.5"/><circle cx="34" cy="28" r="3.5"/><circle cx="15" cy="15" r="6"/><path d="M15 11v4h3"/></g></svg></div>
  <h3>Zero-emission delivery</h3>
  <p>We operate a 100% electric commercial vehicle fleet</p>
</article>
<article class="svc raised" style="left:351px">
  <div class="svc-icon" style="background:var(--lime)"><svg width="40" height="40" viewBox="0 0 40 40"><g fill="none" stroke="#fff" stroke-width="2.2"><circle cx="20" cy="13" r="8"/><path d="M5 38c0-9 7-14 15-14s15 5 15 14"/></g></svg></div>
  <h3>Highly trained delivery drivers</h3>
  <p>We only employ permanently, train far above average, and live a great team spirit</p>
</article>
<article class="svc" style="left:616px">
  <div class="svc-icon" style="background:var(--green)"><svg width="40" height="40" viewBox="0 0 40 40"><g fill="none" stroke="#fff" stroke-width="2.2"><circle cx="20" cy="16" r="12"/><path d="M20 9l2.2 4.5 5 .7-3.6 3.5.9 5-4.5-2.4-4.5 2.4.9-5-3.6-3.5 5-.7z M12 26l-4 10 6-2 3 5 3-9 3 9 3-5 6 2-4-10"/></g></svg></div>
  <h3>Professional all around</h3>
  <p>We honor our commitments and hold ourselves to the highest professional standards</p>
</article>
<article class="svc" style="left:879px">
  <div class="svc-icon" style="background:var(--green)"><svg width="44" height="40" viewBox="0 0 44 40"><g fill="none" stroke="#fff" stroke-width="2.2"><circle cx="16" cy="13" r="7"/><circle cx="30" cy="13" r="7"/><path d="M3 38c0-8 6-13 13-13 M41 38c0-8-6-13-13-13 M12 38c0-6 4-10 10-10s10 4 10 10"/></g></svg></div>
  <h3>Unparalleled customer focus</h3>
  <p>We live a customer-oriented mindset, always measuring ourselves against their experience</p>
</article>

<section class="touch" role="img" aria-label="Photo of hands tending green plants">
  <h2>Get in Touch with Brook Logistics</h2>
  <p>If you got excited, or have a question about our services, our approach, our jobs or just want to get in touch to chat about how green logistics can make the planet a little bit better, please get in touch!</p>
  <div class="btn">Contact Us</div>
</section>

<div class="leaf-left" role="img" aria-label="Green leaves"></div>
<div class="leaf-right" role="img" aria-label="Green leaves"></div>
<h2 class="section-title" style="top:2668px">Careers</h2>
<p class="careers-text" style="top:2726px">If you join Brook Logistics, you join a family. We elevate one another, care for each other's wellbeing and growth, and celebrate our successes. We strongly believe growth is a team sport and that every member of the family fully contributes to the achievements of the company overall.</p>
<p class="careers-text" style="top:2778px">At the heart of everything we do at Brook Logistics is a relentless focus on our mission. That's why we aim to ensure our employees can follow their own passion at the workplace, be this working in a truly collaborative and caring team, putting a smile on a customer's face or making the world a better place.</p>
<p class="careers-text" style="top:2849px">While we are helping our clients grow by delivering their parcels, we are also helping all our employees grow personally and professionally. We care about our employees' happiness and wellbeing which is why we provide additional benefits like supplementary health insurance.</p>
<p class="careers-text" style="top:2902px;font-size:13px">If you are excited about joining our Brook Logistics family, please check out our open positions.</p>
<div class="abs" style="left:168px;top:2940px;width:864px;height:1px;background:var(--line)"></div>
<div class="acc" style="top:2952px;height:74px">
  <h4>Full-time driver / parcel deliverer (m/f/d) for Berlin</h4>
  <p>As a partner for our clients, we are looking for additional members of the Brook Logistics Family in Berlin as soon as possible.</p>
  <span class="plus" style="font-size:18px;color:#555">–</span>
</div>
<div class="acc" style="top:3040px;height:32px"><h4>Your tasks as a delivery driver</h4><span class="plus">+</span></div>
<div class="acc" style="top:3087px;height:32px"><h4>Required knowledge and skills</h4><span class="plus">+</span></div>
<div class="acc" style="top:3134px;height:32px"><h4>What you can expected from the Brook Logistics family</h4><span class="plus">+</span></div>

<section class="contact" role="img" aria-label="Photo of tall green grass rising at the bottom"></section>
<h2 class="section-title" style="top:3312px">We'd Love to Hear From You!</h2>
<p class="abs center" style="left:240px;top:3372px;width:720px;font-size:12px;line-height:18px">Whether you have a question about our services, our approach, our jobs or just want to get in touch to chat about how green logistics can make the planet a little bit better, our team is ready to answer your questions and enquiries.</p>

<div class="contact-icon" style="left:305px"><svg width="24" height="32" viewBox="0 0 24 32"><path d="M12 30S2 18 2 11a10 10 0 0 1 20 0c0 7-10 19-10 19z" fill="none" stroke="#1f9a3f" stroke-width="2"/><circle cx="12" cy="11" r="3.5" fill="none" stroke="#1f9a3f" stroke-width="2"/></svg></div>
<div class="contact-icon" style="left:562px"><svg width="30" height="30" viewBox="0 0 30 30"><path d="M7 2l5 6-3 4c2 4 5 7 9 9l4-3 6 5-3 5C14 28 2 16 3 5z" fill="none" stroke="#1f9a3f" stroke-width="2" stroke-linejoin="round"/></svg></div>
<div class="contact-icon" style="left:809px"><svg width="30" height="22" viewBox="0 0 30 22"><rect x="1" y="1" width="28" height="20" fill="none" stroke="#1f9a3f" stroke-width="2"/><path d="M1 1l14 11L29 1" fill="none" stroke="#1f9a3f" stroke-width="2"/></svg></div>
<div class="contact-label" style="left:232px">1153 Lorem Road Ipsum,<br>Ma-Layout 12345</div>
<div class="contact-label" style="left:482px">Phone:<br>123-456-7890</div>
<div class="contact-label" style="left:729px">Email:<br>info@brooklogistics.com</div>

<div class="field" style="left:233px;top:3605px;width:233px;height:31px">Name</div>
<div class="field" style="left:484px;top:3605px;width:234px;height:31px">Email</div>
<div class="field" style="left:733px;top:3605px;width:234px;height:31px">Phone</div>
<div class="field" style="left:233px;top:3655px;width:734px;height:124px">Type your Message ...</div>
<div class="btn" style="left:536px;top:3798px;width:144px;height:29px;background:var(--green)">Send Message</div>

<div class="footer-line"></div>
<div class="social" style="left:545px"></div>
<div class="social" style="left:586px;background:var(--lime)"></div>
<div class="social" style="left:626px"></div>
<nav class="footer-nav"><span>Home</span><span>About</span><span>Services</span><span>Careers</span><span>Contact</span><span>Legal Notice</span><span>Privacy Policy</span></nav>
<p class="copyright">© 2020 Brook Logistics . All Right Reserved</p>

</body>
</html>
```